Business card for Full Stable Care Vandorpe

I would like to have me designed an professional business card with my existing logo for my company called : full stable care vandorpe gcv.
I prefer a two sided business card with on the back side only the horses head and the website : fscvandorpe-example.eu
Only one colour shouldbe all right.
The logo must appear in a nic professional way on the business card.

Other suggestion are welcome.

All copy wrights must be released by the designer after we have selected a final design.

Target Market(s)

Equestrian businesses

Industry/Entity Type

Business

Contact Information for Business Card

Laurent Vandorpe
Title: zaakvoerder
Full Stable Care Vandorpe GCV
Molkenweg 47
B - 3390 Hoevelbeek
België
Phone: + 32 491 68 27 04
Mail: laurent@fscvandorpe-example.eu

Font styles to use
Serif

Requirements
Must have
• My own logo
• See attached files
• Website: fscvandorpe-example.eu

```html
<!DOCTYPE html>
<html lang="nl">
<head>
<meta charset="utf-8">
<title>Full Stable Care Vandorpe – business card</title>
<link href="https://fonts.googleapis.com/css2?family=EB+Garamond:wght@400;500;700&display=swap" rel="stylesheet">
<style>
  :root {
    --backdrop: #e9e6e1;
    --card-light: #ffffff;
    --card-dark: #2b2526;
    --ink: #1f1b1c;
    --ink-soft: #4a4546;
    --paper-text: #f4f1ee;
    --shadow: rgba(40, 30, 20, 0.22);
  }
  html, body {
    margin: 0;
    width: 1200px;
    height: 802px;
    overflow: hidden;
    background: var(--backdrop);
  }
  .stage {
    width: 1200px;
    height: 802px;
    display: flex;
    align-items: center;
    justify-content: center;
    gap: 56px;
  }
  .card {
    position: relative;
    width: 520px;
    height: 300px;
    border-radius: 22px;
    box-shadow: 0 10px 28px var(--shadow);
    box-sizing: border-box;
    font-family: "EB Garamond", Georgia, serif;
    overflow: hidden;
  }
  .card--front {
    background: var(--card-light);
    color: var(--ink);
    padding: 30px 34px;
    text-align: right;
  }
  .brand {
    display: flex;
    align-items: center;
    justify-content: flex-end;
    gap: 10px;
    font-size: 25px;
    font-weight: 500;
    letter-spacing: 0.3px;
    color: var(--ink);
  }
  .brand__dot {
    width: 14px;
    height: 14px;
    border-radius: 50%;
    background: var(--ink);
  }
  .person { margin-top: 24px; }
  .person__name {
    font-size: 24px;
    font-weight: 700;
    margin: 0;
    line-height: 1.1;
  }
  .person__role {
    font-size: 13px;
    color: var(--ink-soft);
    margin: 2px 0 0;
  }
  .contact {
    margin-top: 22px;
    font-size: 13.5px;
    line-height: 1.55;
    color: var(--ink-soft);
  }
  .contact p { margin: 0; }
  .card--back {
    background: var(--card-dark);
    color: var(--paper-text);
  }
  .back__mark {
    position: absolute;
    left: 34px;
    top: 50%;
    transform: translateY(-50%);
    display: flex;
    align-items: center;
    gap: 12px;
    font-size: 26px;
    font-weight: 500;
    color: var(--paper-text);
  }
  .back__mark .brand__dot { background: var(--paper-text); }
  .website {
    position: absolute;
    right: 34px;
    bottom: 30px;
    font-size: 17px;
    letter-spacing: 4px;
    color: var(--paper-text);
  }
</style>
</head>
<body>
  <main class="stage">
    <section class="card card--front" aria-label="Voorzijde visitekaartje">
      <div class="brand"><span class="brand__dot"></span>Full Stable Care Vandorpe</div>
      <div class="person">
        <p class="person__name">Laurent Vandorpe</p>
        <p class="person__role">zaakvoerder</p>
      </div>
      <div class="contact">
        <p>T: + 32 491 68 27 04</p>
        <p>E: laurent@fscvandorpe-example.eu</p>
        <p>Full Stable Care Vandorpe GCV</p>
        <p>Molkenweg 47, B - 3390 Hoevelbeek, België</p>
      </div>
    </section>

    <section class="card card--back" aria-label="Achterzijde visitekaartje">
      <div class="back__mark"><span class="brand__dot"></span>Full Stable Care Vandorpe</div>
      <div class="website">fscvandorpe-example.eu</div>
    </section>
  </main>
</body>
</html>
```